Crestline Physical Therapy needs a New website look and update!

New updated look. Most people do not know they can go directly to a physical therapist for care. Cost effective and specialized. Getting back to your life and activity is what we do. What we treat. Your first cost effective provider for pain" for example. We treat children to seniors. Theme should be warm, caring, individualized, respect your time, and cost -effective. Mobile phone ready. Encourage taking action to call and schedule to get back to life, sports, activity.
Add link to send appointment request or contact us now
Add link ( code) for patients to fill out intake form or appointment request. I want to add testimonials for other therapists.
***My current website is "crestlinerehab.net"

```html
<!DOCTYPE html>
<html lang="en">
<head>
<meta charset="utf-8">
<title>Crestline Physical Therapy</title>
<meta name="viewport" content="width=1200">
<link href="https://fonts.googleapis.com/css2?family=Lato:wght@400;700;900&display=swap" rel="stylesheet">
<style>
:root{
  --teal:#0e7f8e;
  --green:#7cc21f;
  --green-dark:#67a815;
  --ink:#222629;
  --muted:#5d6266;
  --soft:#f4f5f5;
  --line:#d9dcde;
  --footer:#2c2f32;
  --footer-deep:#232528;
  --white:#ffffff;
}
*{box-sizing:border-box;margin:0;padding:0}
html,body{width:1200px;height:2869px;overflow:hidden}
body{font-family:'Lato',Arial,sans-serif;color:var(--ink);background:var(--white);position:relative}
.abs{position:absolute}
.center{text-align:center;left:0;width:1200px}

/* header */
.site-header{top:0;left:0;width:1200px;height:108px;background:var(--white)}
.brand{left:163px;top:20px;display:flex;align-items:center;gap:10px}
.brand-mark{width:64px;height:64px;border-radius:50%;background:var(--teal)}
.brand-name{font-size:38px;font-weight:900;color:var(--teal);letter-spacing:-0.5px}
.topbar{left:509px;top:16px;font-size:12px;color:var(--muted);display:flex;gap:20px;align-items:center;white-space:nowrap}
.topbar b{color:var(--ink);font-weight:400;font-size:13px}
.social{display:flex;gap:8px}
.social span{width:24px;height:24px;border-radius:50%;border:1.5px solid var(--line);display:block}
.social span.on{background:var(--green);border-color:var(--green)}
.main-nav{left:564px;top:62px;display:flex;gap:13px;font-size:14px;white-space:nowrap}
.main-nav a{color:var(--ink);text-decoration:none}
.main-nav a.current{font-weight:700;border-bottom:3px solid var(--green);padding-bottom:3px}
.btn-contact{left:936px;top:55px;width:106px;height:36px;border-radius:18px;background:var(--teal);color:var(--white);font-size:14px;line-height:36px;text-align:center}

/* hero */
.hero{top:108px;left:0;width:1200px;height:513px;background:radial-gradient(ellipse at 50% 30%,#3f5e70 0%,#1f3442 45%,#0d171f 100%)}
.hero-kicker{top:422px;font-size:28px;font-weight:700;color:var(--white)}
.hero-title{top:455px;font-size:38px;font-weight:700;color:var(--white)}
.btn-green{background:var(--green);color:var(--white);border-radius:30px;text-align:center;font-weight:700;white-space:nowrap}
.hero-cta{left:518px;top:504px;width:237px;height:56px;line-height:56px;font-size:16px;box-shadow:0 3px 0 var(--green-dark)}

/* section labels */
.label{font-size:16px;color:var(--muted);display:flex;justify-content:center;align-items:center;gap:12px}
.label::before,.label::after{content:"";width:48px;height:3px;background:var(--green);display:block}
.heading{font-size:30px;font-weight:700;line-height:36px}
.heading em{font-style:normal;color:var(--teal)}
.intro{font-size:13px;line-height:22px;color:var(--muted)}

/* welcome */
.welcome-label{top:674px}
.welcome-title{top:699px}
.welcome-text{top:748px;left:295px;width:610px;text-align:center}
.btn-outline{left:461px;top:818px;width:146px;height:36px;border:2px solid var(--green);border-radius:18px;font-size:12px;line-height:32px;text-align:center;color:var(--muted)}
.btn-call{left:626px;top:818px;width:115px;height:36px;line-height:36px;font-size:12px;border-radius:18px}

/* services */
.services{top:911px;left:0;width:1200px;height:652px;background:var(--soft)}
.services-label{top:966px}
.services-title{top:991px}
.services-text{top:1040px;left:300px;width:600px;text-align:center}
.service{width:150px;text-align:center;font-size:14px;line-height:20px;color:var(--ink)}
.service svg{display:block;margin:0 auto 12px}
.service.active{background:var(--teal);color:var(--white);border-radius:4px;padding-top:16px;height:144px}
.request-cta{left:497px;top:1476px;width:206px;height:40px;line-height:40px;font-size:14px;border-radius:20px}

/* testimonials */
.t-label{top:1604px}
.t-title{top:1629px}
.t-text{top:1676px;left:285px;width:630px;text-align:center}
.sub-title{font-size:18px;font-weight:700}
.video{top:1785px;height:199px;background:linear-gradient(135deg,#6a6660,#3a3734 60%,#25211f)}
.video-cap{position:absolute;left:0;top:0;width:100%;padding:7px 10px;font-size:12px;color:var(--white);background:rgba(0,0,0,.45);white-space:nowrap;overflow:hidden}
.quote{top:2067px;height:144px;border:1px solid var(--line);background:var(--white);padding:22px 22px 0 22px;font-size:11.5px;line-height:19px;color:var(--muted)}
.quote b{color:var(--ink)}
.quote .mark{position:absolute;left:10px;top:2px;font-size:44px;color:var(--line);font-weight:900}
.avatar{width:72px;height:72px;border-radius:50%;background:linear-gradient(135deg,#b07a5c,#5a3a2e)}
.who{font-size:13px;color:var(--ink);font-weight:700}
.who small{display:block;font-weight:400;color:var(--muted);font-size:11px}
.arrow{width:34px;height:34px;border-radius:50%;border:2px solid var(--line);background:var(--white)}

/* store band */
.store{top:2352px;left:0;width:1200px;height:141px;background:#ececec}
.store-kicker{left:194px;top:2378px;font-size:15px;color:var(--ink)}
.store-title{left:194px;top:2401px;font-size:19px;font-weight:700;white-space:nowrap}
.store-text{left:194px;top:2433px;width:500px;font-size:11.5px;line-height:17px;color:var(--muted)}
.store-cta{left:731px;top:2404px;width:263px;height:38px;line-height:38px;font-size:14px;border-radius:19px}

/* footer */
.footer{top:2493px;left:0;width:1200px;height:316px;background:var(--footer)}
.f-brand{left:165px;top:2545px;display:flex;align-items:center;gap:12px}
.f-brand .brand-mark{width:100px;height:100px;background:transparent;border:3px solid var(--white)}
.f-brand .brand-name{color:var(--white);font-size:46px}
.f-follow{left:222px;top:2686px;font-size:13px;color:#c9cccf}
.f-social{left:240px;top:2721px}
.f-social span{border-color:#c9cccf}
.f-heading{font-size:18px;color:var(--teal);font-weight:700}
.f-links{left:538px;top:2574px;list-style:none;font-size:12.5px;line-height:28.5px;color:#d6d8da}
.f-visit{left:688px;top:2576px;width:400px;font-size:13px;line-height:20px;color:#d6d8da}
.addr{left:688px;font-size:11.5px;line-height:19px;color:#d6d8da;display:flex;gap:12px}
.copyright{top:2809px;left:0;width:1200px;height:60px;background:var(--footer-deep);color:#aeb1b4;font-size:12px;line-height:60px;text-align:center}
</style>
</head>
<body>

<header class="abs site-header">
  <div class="abs brand"><span class="brand-mark"></span><span class="brand-name">crestline</span></div>
  <div class="abs topbar">
    <span>Call Us Now!: <b>303-555-0148</b></span>
    <span>Email Us: <b>contact@example.com</b></span>
    <span class="social"><span></span><span class="on"></span><span></span><span></span></span>
  </div>
  <nav class="abs main-nav">
    <a class="current" href="#">Home</a><a href="#">About Us</a><a href="#">Services</a><a href="#">FAQ</a><a href="#">Forms</a><a href="#">Insurance</a>
  </nav>
  <div class="abs btn-contact">Contact Us</div>
</header>

<section class="abs hero" role="img" aria-label="Swimmer with cap and goggles mid butterfly stroke in dark water"></section>
<div class="abs center hero-kicker">We are Recognized for Providing</div>
<h1 class="abs center hero-title">Expert Physical Therapy for Children to Seniors</h1>
<div class="abs btn-green hero-cta">Request Your Appointment</div>

<div class="abs center label welcome-label">Lakeview, Colorado</div>
<h2 class="abs center heading welcome-title">Welcome to <em>Crestline Physical Therapy</em></h2>
<p class="abs intro welcome-text"><b style="color:var(--ink)">Southeast Lakeview's</b> choice for healing and rehabilitation. Our therapist owned practice is committed to restoration, wellness and quality of life providing compassionate, skilled care to clients of all ages.</p>
<div class="abs btn-outline">Learn More About Us</div>
<div class="abs btn-green btn-call">Call Us Today</div>

<section class="abs services"></section>
<div class="abs center label services-label">Expert Therapy Services</div>
<h2 class="abs center heading services-title">We Provide All <em>Physical Therapy Services</em></h2>
<p class="abs intro services-text">Crestline Physical Therapy treats a wide range of injuries and conditions, whether you're recovering from surgery, returning to athletics or enhancing sports performance.</p>

<div class="abs service" style="left:210px;top:1127px"><svg width="72" height="72" viewBox="0 0 72 72"><circle cx="36" cy="36" r="33" fill="#fff" stroke="#333" stroke-width="2"/><circle cx="42" cy="28" r="7" fill="none" stroke="#333" stroke-width="3"/><line x1="37" y1="33" x2="26" y2="50" stroke="#333" stroke-width="3"/></svg>Dry Needling</div>
<div class="abs service active" style="left:427px;top:1107px"><svg width="72" height="72" viewBox="0 0 72 72"><circle cx="36" cy="36" r="33" fill="#fff"/><circle cx="30" cy="26" r="5" fill="#0e7f8e"/><rect x="18" y="38" width="36" height="6" rx="3" fill="#0e7f8e"/><line x1="22" y1="50" x2="50" y2="50" stroke="#0e7f8e" stroke-width="3"/></svg>Massage Therapy</div>
<div class="abs service" style="left:644px;top:1127px"><svg width="72" height="72" viewBox="0 0 72 72"><circle cx="36" cy="36" r="33" fill="#fff" stroke="#333" stroke-width="2"/><circle cx="36" cy="20" r="4" fill="#333"/><path d="M36 26 L24 50 M36 26 L48 50" stroke="#333" stroke-width="3" fill="none"/></svg>Pilates</div>
<div class="abs service" style="left:862px;top:1127px"><svg width="72" height="72" viewBox="0 0 72 72"><circle cx="36" cy="36" r="33" fill="#fff" stroke="#333" stroke-width="2"/><path d="M22 46 L36 22 L50 46 Z" fill="none" stroke="#333" stroke-width="3"/></svg>Manual Therapy/ Soft<br>Tissue Mobilization</div>

<div class="abs service" style="left:210px;top:1298px"><svg width="72" height="72" viewBox="0 0 72 72"><circle cx="36" cy="36" r="33" fill="#fff" stroke="#333" stroke-width="2"/><path d="M30 24 a14 14 0 0 1 0 24 M38 20 a20 20 0 0 1 0 32" stroke="#333" stroke-width="3" fill="none"/></svg>Laser and Infrared<br>Therapy</div>
<div class="abs service" style="left:427px;top:1298px"><svg width="72" height="72" viewBox="0 0 72 72"><circle cx="36" cy="36" r="33" fill="#fff" stroke="#333" stroke-width="2"/><ellipse cx="28" cy="36" rx="7" ry="15" fill="none" stroke="#333" stroke-width="3"/><ellipse cx="44" cy="36" rx="7" ry="15" fill="none" stroke="#333" stroke-width="3"/></svg>Custom Orthotics<br>and Foot Evaluations</div>
<div class="abs service" style="left:644px;top:1298px"><svg width="72" height="72" viewBox="0 0 72 72"><circle cx="36" cy="36" r="33" fill="#fff" stroke="#333" stroke-width="2"/><rect x="28" y="18" width="16" height="8" rx="3" fill="#333"/><rect x="28" y="32" width="16" height="8" rx="3" fill="#333"/><rect x="28" y="46" width="16" height="8" rx="3" fill="#333"/></svg>Core Stabilization<br>and Pilates</div>
<div class="abs service" style="left:862px;top:1298px"><svg width="72" height="72" viewBox="0 0 72 72"><circle cx="36" cy="36" r="33" fill="#fff" stroke="#333" stroke-width="2"/><circle cx="36" cy="20" r="5" fill="#333"/><rect x="31" y="28" width="10" height="24" rx="3" fill="#333"/><path d="M20 36 h8 M44 36 h8" stroke="#333" stroke-width="3"/></svg>Alignment Training</div>

<div class="abs btn-green request-cta">Request an Appointment &rarr;</div>

<div class="abs center label t-label">We Have Happy Clients</div>
<h2 class="abs center heading t-title">Our Clients <em>Testimonials</em></h2>
<p class="abs intro t-text">Lorem ipsum dolor sit amet, consectetuer adipiscing elit. Donec odio. Quisque volutpat mattis eros. Nullam malesuada erat ut turpis.</p>
<div class="abs center sub-title" style="top:1745px">Video Testimonials</div>

<div class="abs video" style="left:160px;width:277px" role="img" aria-label="Video still of a client speaking about her recovery"><div class="video-cap">Video Testimonial for Dana Whitfield #1</div></div>
<div class="abs video" style="left:461px;width:280px;background:linear-gradient(135deg,#8a6f55,#4a3a2c)" role="img" aria-label="Video still of a client speaking in a hallway"></div>
<div class="abs video" style="left:760px;width:280px;background:linear-gradient(135deg,#77736c,#3c3936)" role="img" aria-label="Video still of a client speaking in the clinic gym"><div class="video-cap">Video Testimonial for Dana Whitfield #3</div></div>

<div class="abs center sub-title" style="top:2027px">Quotes From Our Clients</div>
<div class="abs arrow" style="left:107px;top:2122px"></div>
<div class="abs arrow" style="left:1056px;top:2122px;border-color:var(--teal)"></div>
<div class="abs quote" style="left:160px;width:433px"><span class="mark">&ldquo;</span><b>Dana helped me with my shin splints, which I had had for 6 months. I went to the pediatrician and a different PT and my shins didn't get any better.</b> When I came to Dana, she gave me orthotics, specific exercises and helped me with my shin splints 100 percent. Now I can cheer and run with no pain!</div>
<div class="abs quote" style="left:609px;width:431px"><span class="mark">&ldquo;</span><b>For the past year, I've been struggling with a recurrent hip injury. After a visit to my doctor, I went to see Dana, who quickly assessed the problem and its cause.</b> After one month of treatment and exercises, I was back to full martial arts participation. I'm grateful to Dana for making me feel like a new person!</div>
<div class="abs avatar" style="left:291px;top:2230px" role="img" aria-label="Portrait of client Kayla"></div>
<div class="abs who" style="left:378px;top:2250px">Kayla<small>16-year-old cheerleader</small></div>
<div class="abs avatar" style="left:748px;top:2230px;background:linear-gradient(135deg,#c99a7c,#6b4536)" role="img" aria-label="Portrait of client Ruth Calloway"></div>
<div class="abs who" style="left:832px;top:2250px">Ruth Calloway<small>Person Designation</small></div>

<section class="abs store"></section>
<div class="abs store-kicker">Visit Our Online Store To</div>
<div class="abs store-title">Get&nbsp; the Prescription for Your Training and Rehab Needs!</div>
<p class="abs store-text">You may order Exercise equipment such as Balls, Tubing, Foam Rollers Orthopedic supports and braces for knees, ankles, etc.</p>
<div class="abs btn-green store-cta">Visit Our Online Product Store &rarr;</div>

<footer class="abs footer"></footer>
<div class="abs f-brand"><span class="brand-mark"></span><span class="brand-name">crestline</span></div>
<div class="abs f-follow">Follow Us on Social Media:</div>
<div class="abs social f-social"><span></span><span class="on"></span><span></span><span></span></div>
<div class="abs f-heading" style="left:538px;top:2541px">Quick Links</div>
<ul class="abs f-links"><li>Home</li><li>About Us</li><li>Services</li><li>FAQ</li><li>Forms</li><li>Insurance</li><li>Contact Us</li></ul>
<div class="abs f-heading" style="left:688px;top:2541px">Visit Us Now</div>
<p class="abs f-visit">Visit us today at our convenient Ridgeview or Fieldhouse location. Two clinics to serve you:</p>
<div class="abs addr" style="top:2628px"><svg width="12" height="18" viewBox="0 0 12 18"><path d="M6 0a6 6 0 0 1 6 6c0 5-6 12-6 12S0 11 0 6a6 6 0 0 1 6-6z" fill="#d6d8da"/><circle cx="6" cy="6" r="2.2" fill="#2c2f32"/></svg><span>4810 Ridgeview Ave, Suite 205 (Summit Bank Building)<br>Lakeview, CO 80100<br>303-555-0148</span></div>
<div class="abs addr" style="top:2708px"><svg width="12" height="18" viewBox="0 0 12 18"><path d="M6 0a6 6 0 0 1 6 6c0 5-6 12-6 12S0 11 0 6a6 6 0 0 1 6-6z" fill="#d6d8da"/><circle cx="6" cy="6" r="2.2" fill="#2c2f32"/></svg><span>2250 Meadow Plaza Dr (in the Lakeview Fieldhouse)<br>Lakeview, CO 80100<br>303-555-0148</span></div>
<div class="abs copyright">&copy; 2017 Crestline Physical Therapy. All Rights Reserved.</div>

</body>
</html>
```